Software company specialized in data analytics and professional services

We need a landing page design for our business. It should include our logo design. It should have multiple sections :
- stylish head
- what we do (data analytics software, professional services)
- contact form

Target Market(s)

Companies, B2B

Industry/Entity Type

Data

Number of Pages Required

1 page

Font styles to use
Sans Serif

Requirements
Must have
• Dark theme
Should not have
• Gradients on buttons

```html
<!DOCTYPE html>
<html lang="en">
<head>
<meta charset="utf-8">
<title>Velqor — Data Analytics &amp; Professional Services</title>
<link href="https://fonts.googleapis.com/css2?family=Montserrat:wght@700;800;900&family=Inter:wght@400;500;600;700&display=swap" rel="stylesheet">
<style>
:root{
  --bg:#0f0a30;
  --bg-field:#1b1740;
  --magenta:#e8088f;
  --teal:#0b7ea8;
  --purple:#8b14cf;
  --navy:#1c1a6a;
  --white:#ffffff;
  --muted:#c9c6dc;
  --line:#2a2550;
}
*{box-sizing:border-box;margin:0;padding:0}
html,body{width:1200px;height:3484px;overflow:hidden;background:var(--bg);color:var(--white);font-family:"Inter",sans-serif}
a{text-decoration:none;color:var(--white)}
.page{position:relative;width:1200px;height:3484px;overflow:hidden}
.abs{position:absolute}
.logo{font-family:"Inter",sans-serif;font-weight:700;font-size:30px;letter-spacing:2px;color:var(--white)}
.nav{position:absolute;top:47px;left:337px;display:flex;gap:29px;font-size:11px;letter-spacing:.3px;color:var(--white)}
.btn{position:absolute;display:flex;align-items:center;justify-content:center;gap:8px;font-family:"Inter",sans-serif;font-weight:700;font-size:13px;text-transform:uppercase;color:var(--white);border-radius:3px}
.btn svg{width:16px;height:10px}
.btn-solid{background:var(--magenta)}
.btn-outline{border:2px solid var(--purple);background:transparent}
.hero-title{position:absolute;top:178px;left:0;width:1200px;text-align:center;font-family:"Montserrat",sans-serif;font-weight:800;font-size:60px;line-height:60px;letter-spacing:-1px}
.teal{color:var(--teal)}
.pink{color:var(--magenta)}
.hero-text{position:absolute;top:314px;left:282px;width:636px;text-align:center;font-size:13px;line-height:20px;color:var(--white)}
.hero-art{position:absolute;left:140px;top:520px;width:900px;height:465px;border-radius:8px;background:radial-gradient(ellipse at 50% 45%,#3a2f86 0%,#251c63 45%,#15103f 100%)}
.sec-title{position:absolute;left:62px;top:1078px;font-family:"Montserrat",sans-serif;font-weight:900;font-size:68px;line-height:60px}
.sec-text{position:absolute;left:62px;top:1208px;width:300px;font-size:13px;line-height:17.5px}
.card{position:absolute;width:296px;height:342px;border:2px solid var(--purple);border-radius:3px;padding:22px 22px;display:flex;flex-direction:column}
.card .icon{flex:none;width:62px;height:62px;border:2px solid var(--magenta);border-radius:50%;opacity:.85}
.card h3{margin-top:18px;font-family:"Montserrat",sans-serif;font-weight:800;font-size:20px;color:var(--teal)}
.card p{margin-top:6px;font-size:12.5px;line-height:17.5px;color:var(--white)}
.card .more{margin-top:16px;display:flex;align-items:center;gap:6px;font-size:13px;font-weight:700;color:var(--magenta)}
.card .more svg{width:16px;height:10px}
.contact-title{position:absolute;top:2250px;width:1200px;text-align:center;font-family:"Montserrat",sans-serif;font-weight:900;font-size:60px}
.contact-text{position:absolute;top:2334px;left:340px;width:520px;text-align:center;font-size:13.5px;line-height:19px}
.field{position:absolute;width:345px;height:54px;background:var(--bg-field);border-radius:4px;padding:19px 21px;font-size:14.5px;color:var(--muted)}
.field.active{border:2px solid var(--purple);padding:17px 19px}
.field.message{width:718px;height:108px}
.check{position:absolute;left:241px;top:2804px;width:24px;height:24px;border:2px solid #5b5780;border-radius:3px}
.consent{position:absolute;left:280px;top:2798px;width:690px;font-size:14px;line-height:19px;color:var(--muted)}
.rule{position:absolute;left:62px;top:3018px;width:1076px;height:1px;background:var(--line)}
.f-col{position:absolute;top:3098px}
.f-col h4{font-family:"Inter",sans-serif;font-weight:700;font-size:18px;padding-bottom:9px;border-bottom:3px solid var(--purple);width:156px}
.f-col ul{list-style:none;margin-top:18px}
.f-col li{font-size:17px;color:var(--muted);height:34.5px;display:flex;align-items:center;gap:12px;white-space:nowrap}
.f-col li svg{width:17px;height:17px}
.bottom{position:absolute;top:3448px;font-size:13.5px;color:var(--muted)}
.social{position:absolute;top:3447px;width:18px;height:18px;background:var(--white)}
.side-deco{position:absolute;width:122px;height:310px}
</style>
</head>
<body>
<div class="page">

  <!-- side decorations -->
  <div class="side-deco" role="img" aria-label="Decorative side shapes in teal, purple and navy" style="left:0;top:2310px;border-radius:0 40px 40px 0;background:linear-gradient(180deg,rgba(11,126,168,.35) 0%,rgba(139,20,207,.35) 50%,rgba(28,26,106,.5) 100%)"></div>
  <div class="side-deco" role="img" aria-label="Decorative side shapes in navy, magenta and teal" style="left:1078px;top:2533px;border-radius:40px 0 0 40px;background:linear-gradient(180deg,rgba(28,26,106,.5) 0%,rgba(232,8,143,.35) 50%,rgba(11,126,168,.35) 100%)"></div>

  <!-- header -->
  <div class="abs logo" style="left:62px;top:36px">VELQOR</div>
  <nav class="nav">
    <span>ABOUT US</span><span>SERVICES</span><span>INDUSTRIES</span><span>CASE STUDIES</span><span>INSIGHTS</span><span>CONTACT US</span>
  </nav>
  <a class="btn btn-solid" style="left:952px;top:31px;width:163px;height:46px;font-size:11.5px">Get in touch
    <svg viewBox="0 0 16 10"><path d="M0 5h14M10 1l4 4-4 4" stroke="#fff" stroke-width="1.6" fill="none"/></svg></a>

  <!-- hero -->
  <h1 class="hero-title">Transform <span class="teal">Raw Data</span> into<br><span class="pink">Business Insights</span></h1>
  <p class="hero-text">Unlock the power of your data with Velqor, a leading software company specializing in data analytics and other professional services. At Velqor, we believe in transforming raw data into actionable insights, empowering businesses to make informed decisions and drive success.</p>
  <a class="btn btn-outline" style="left:392px;top:403px;width:192px;height:53px">Our services
    <svg viewBox="0 0 16 10"><path d="M0 5h14M10 1l4 4-4 4" stroke="#fff" stroke-width="1.6" fill="none"/></svg></a>
  <a class="btn btn-outline" style="left:616px;top:403px;width:192px;height:53px;border-color:var(--magenta)">Contact us
    <svg viewBox="0 0 16 10"><path d="M0 5h14M10 1l4 4-4 4" stroke="#fff" stroke-width="1.6" fill="none"/></svg></a>
  <div class="hero-art" role="img" aria-label="Illustration of a laptop showing analytics dashboards with a magnifying glass, server racks, a folder, report sheets and a plant"></div>

  <!-- services -->
  <h2 class="sec-title">Our<br><span class="teal">Services</span></h2>
  <p class="sec-text">Explore a world of possibilities with Velqor – your trusted partner in navigating the data landscape and unlocking the true potential of your business.</p>
  <a class="btn btn-solid" style="left:62px;top:1306px;width:194px;height:51px">Contact us
    <svg viewBox="0 0 16 10"><path d="M0 5h14M10 1l4 4-4 4" stroke="#fff" stroke-width="1.6" fill="none"/></svg></a>

  <div class="card" style="left:842px;top:1085px">
    <div class="icon" role="img" aria-label="Data governance icon"></div>
    <h3>Data Governance</h3>
    <p>Velqor's Data Governance services establish and uphold the principles of data integrity, quality, and compliance. We guide you through the creation and implementation of effective governance policies, ensuring your data speaks with ac...</p>
    <span class="more">LEARN MORE <svg viewBox="0 0 16 10"><path d="M0 5h14M10 1l4 4-4 4" stroke="#e8088f" stroke-width="1.6" fill="none"/></svg></span>
  </div>

  <div class="card" style="left:452px;top:1258px">
    <div class="icon" role="img" aria-label="Data analytics icon"></div>
    <h3>Data Analytics</h3>
    <p>At Velqor, we excel in the art of deciphering data. Our Data Analytics services go beyond mere numbers, transforming raw information into actionable insights. Whether it's predictive modeling, trend analysis, or reporting, our team ensures your data becom...</p>
    <span class="more">LEARN MORE <svg viewBox="0 0 16 10"><path d="M0 5h14M10 1l4 4-4 4" stroke="#e8088f" stroke-width="1.6" fill="none"/></svg></span>
  </div>

  <div class="card" style="left:62px;top:1430px">
    <div class="icon" role="img" aria-label="Data engineering icon"></div>
    <h3>Data Engineering</h3>
    <p>Building a robust data foundation is key to unlocking analytics potential. Velqor's Data Engineering services specialize in seamless data integration, migration, and warehousing. Our team architects scalable solutions, ensuring your data infrastructure is...</p>
    <span class="more">LEARN MORE <svg viewBox="0 0 16 10"><path d="M0 5h14M10 1l4 4-4 4" stroke="#e8088f" stroke-width="1.6" fill="none"/></svg></span>
  </div>

  <div class="card" style="left:842px;top:1488px">
    <div class="icon" role="img" aria-label="Cloud computing icon"></div>
    <h3>Cloud Computing</h3>
    <p>Elevate your operations with Velqor's Cloud Computing services. Our experts seamlessly transition your infrastructure to the cloud, providing scalability, flexibility, and cost-efficiency. Whether it's migrating systems or developing cloud-native applications...</p>
    <span class="more">LEARN MORE <svg viewBox="0 0 16 10"><path d="M0 5h14M10 1l4 4-4 4" stroke="#e8088f" stroke-width="1.6" fill="none"/></svg></span>
  </div>

  <div class="card" style="left:452px;top:1661px">
    <div class="icon" role="img" aria-label="Cyber security icon"></div>
    <h3>Cyber Security</h3>
    <p>Security is at the core of everything we do. Velqor's Cyber Security services are designed to safeguard your valuable data assets. From threat assessments to robust encryption, we deploy cutting-edge measures against cyber threats. Trust us to fortify your digita...</p>
    <span class="more">LEARN MORE <svg viewBox="0 0 16 10"><path d="M0 5h14M10 1l4 4-4 4" stroke="#e8088f" stroke-width="1.6" fill="none"/></svg></span>
  </div>

  <div class="card" style="left:62px;top:1835px">
    <div class="icon" role="img" aria-label="AI and machine learning icon"></div>
    <h3>AI / ML</h3>
    <p>Embrace the future with Velqor's AI/ML services. We bring the power of artificial intelligence and machine learning to your fingertips, enabling you to glean insights, predict trends, and automate processes. From recommendations to anomaly detection, our solutions open...</p>
    <span class="more">LEARN MORE <svg viewBox="0 0 16 10"><path d="M0 5h14M10 1l4 4-4 4" stroke="#e8088f" stroke-width="1.6" fill="none"/></svg></span>
  </div>

  <!-- contact -->
  <h2 class="contact-title">Contact Us Today!</h2>
  <p class="contact-text">Explore the full potential of your data with Velqor. Schedule a consultation with us today and unlock valuable insights for your business.</p>
  <div class="field active" style="left:241px;top:2411px">First Name*</div>
  <div class="field" style="left:616px;top:2411px">Last Name*</div>
  <div class="field" style="left:241px;top:2495px">Email Address*</div>
  <div class="field" style="left:616px;top:2495px">Phone Number*</div>
  <div class="field" style="left:241px;top:2579px">Company Name*</div>
  <div class="field" style="left:616px;top:2579px">Subject*</div>
  <div class="field message" style="left:241px;top:2663px">Message*</div>
  <div class="check"></div>
  <p class="consent">I agree to allow Velqor to use my personal information to send me electronic messages and marketing communications as described in the Privacy Policy.</p>
  <a class="btn btn-solid" style="left:511px;top:2874px;width:194px;height:52px">Submit
    <svg viewBox="0 0 16 10"><path d="M0 5h14M10 1l4 4-4 4" stroke="#fff" stroke-width="1.6" fill="none"/></svg></a>

  <!-- footer -->
  <div class="rule"></div>
  <div class="abs logo" style="left:62px;top:3100px">VELQOR</div>
  <div class="f-col" style="left:355px">
    <h4>MAIN LINKS</h4>
    <ul><li>About Us</li><li>Services</li><li>Industries</li><li>Case Studies</li><li>Insights</li><li>Contact Us</li></ul>
  </div>
  <div class="f-col" style="left:628px">
    <h4>SERVICES</h4>
    <ul><li>Data Analytics</li><li>Data Governance</li><li>Cyber Security</li><li>Cloud Computing</li><li>AI / ML</li><li>Data Engineering</li></ul>
  </div>
  <div class="f-col" style="left:901px">
    <h4>CONTACT US</h4>
    <ul>
      <li><svg viewBox="0 0 18 18"><rect x="1" y="4" width="16" height="11" rx="1" fill="#e8088f"/><path d="M1 5l8 6 8-6" stroke="#0f0a30" stroke-width="1.4" fill="none"/></svg>hello@velqor.example</li>
      <li><svg viewBox="0 0 18 18"><path d="M4 2l3 0 1 4-2 1.5c1 2 2.5 3.5 4.5 4.5L12 10l4 1v3c0 1-1 2-2 2C8 16 2 10 2 4c0-1 1-2 2-2z" fill="#e8088f"/></svg>+1 555 010 2040</li>
      <li><svg viewBox="0 0 18 18"><path d="M9 1a6 6 0 0 1 6 6c0 4.5-6 10-6 10S3 11.5 3 7a6 6 0 0 1 6-6z" fill="#e8088f"/><circle cx="9" cy="7" r="2.3" fill="#0f0a30"/></svg>Your Office Address Here</li>
    </ul>
  </div>
  <p class="bottom" style="left:64px">©2023 Velqor. All rights reserved.</p>
  <p class="bottom" style="left:497px">Privacy Policy</p>
  <div class="abs" style="left:601px;top:3444px;width:1px;height:22px;background:#6a6690"></div>
  <p class="bottom" style="left:617px">Terms of Use</p>
  <div class="social" style="left:1091px;border-radius:50%"></div>
  <div class="social" style="left:1118px;border-radius:2px"></div>

</div>
</body>
</html>
```